Professional Home Buyer business card needed

I need a pretty straight forward business card designed. We help people that NEED to sell their homes solve problems. We perform all types of Real Estate transactions including flip, wholesale, investment, rental property and multi family. The card will mainly be used to give to prospective Sellers but will also be given to Real Estate Investors as well. It should professional and very easy to read, most clients are older people.

Target Market(s)

Distressed home sellers as well as Real Estate investors

Industry/Entity Type

Real Estate

Contact Information for Business Card

should be a professional layout

Colors
ec1f27
ffffff
000000

Requirements
Must have
• Large logo on back and smaller one on front. should utilize Red, white, and black.
• I am thinking of using a soft touch coating on the card so keep that in mind.
• Contact info should be very easy to read, think older clients.
Nice to have
• I would like to see a design with rounded corners on the card
Should not have
• pictures of homes or other home graphics.

```html
<!DOCTYPE html>
<html lang="en">
<head>
<meta charset="UTF-8">
<title>Keystone Home Buyers – Business Card</title>
<link href="https://fonts.googleapis.com/css2?family=Montserrat:wght@500;700;800&family=Source+Sans+3:wght@400&display=swap" rel="stylesheet">
<style>
  :root {
    --red: #ff0000;
    --black: #000000;
    --ink: #231f20;
    --white: #ffffff;
    --text: #3a3a3a;
    --stage-light: #e8e9ea;
    --stage-dark: #d0d1d3;
  }
  * { box-sizing: border-box; margin: 0; padding: 0; }
  html, body { width: 800px; height: 1200px; overflow: hidden; }
  body {
    position: relative;
    background: radial-gradient(circle at 50% 50%, var(--stage-light) 0%, var(--stage-dark) 75%);
    font-family: "Source Sans 3", sans-serif;
  }
  .card {
    position: absolute;
    width: 505px;
    height: 288px;
  }
  .card--front {
    left: 152px; top: 170px;
    background: var(--white);
    box-shadow: 0 0 1px rgba(0,0,0,0.15);
  }
  .card--back {
    left: 148px; top: 704px;
    width: 504px;
    background: var(--ink);
  }
  .rule {
    position: absolute; left: 0; right: 0;
    height: 2px; background: var(--black);
  }
  .rule--top { top: 17px; }
  .rule--bottom { top: 100px; }
  .name-band {
    position: absolute; left: 0; right: 0; top: 21px; height: 77px;
    background: var(--red);
    color: var(--white);
    text-align: center;
    font-family: "Montserrat", sans-serif;
  }
  .name-band__name {
    margin-top: 19px;
    font-size: 23px; font-weight: 500; letter-spacing: 0.2px;
  }
  .name-band__title {
    margin-top: 2px;
    font-size: 12px; font-weight: 500;
  }
  .brand {
    position: absolute;
    display: flex; align-items: center; gap: 10px;
    font-family: "Montserrat", sans-serif;
    font-weight: 800;
    text-transform: uppercase;
  }
  .brand__mark { flex: none; background: var(--red); }
  .brand--front {
    left: 30px; top: 170px; width: 180px;
    color: var(--black);
    font-size: 19px; line-height: 1.05;
  }
  .brand--front .brand__mark { width: 20px; height: 20px; }
  .brand--back {
    left: 0; right: 0; top: 112px;
    justify-content: center;
    color: var(--white);
    font-size: 34px; letter-spacing: 1px;
  }
  .brand--back .brand__mark { width: 34px; height: 34px; }
  .divider {
    position: absolute; left: 237px; top: 161px;
    width: 1px; height: 90px;
    background: linear-gradient(to bottom, transparent, #555 50%, transparent);
  }
  .contact-list {
    position: absolute; left: 276px; top: 166px;
    list-style: none;
  }
  .contact-list__item {
    display: flex; align-items: center;
    height: 30px;
    font-size: 14px; color: var(--text);
  }
  .contact-list__icon {
    width: 11px; height: 11px; margin-right: 6px; flex: none;
    fill: var(--text);
  }
</style>
</head>
<body>
  <section class="card card--front" aria-label="Business card front">
    <div class="rule rule--top"></div>
    <header class="name-band">
      <p class="name-band__name">Daniel Harrow</p>
      <p class="name-band__title">Managing Member</p>
    </header>
    <div class="rule rule--bottom"></div>

    <div class="brand brand--front">
      <span class="brand__mark"></span>
      <span class="brand__name">Keystone Home Buyers</span>
    </div>

    <div class="divider"></div>

    <ul class="contact-list">
      <li class="contact-list__item">
        <svg class="contact-list__icon" viewBox="0 0 24 24" aria-hidden="true"><path d="M6.6 10.8a15.1 15.1 0 0 0 6.6 6.6l2.2-2.2a1 1 0 0 1 1-.25 11.4 11.4 0 0 0 3.6.57 1 1 0 0 1 1 1V20a1 1 0 0 1-1 1A17 17 0 0 1 3 4a1 1 0 0 1 1-1h3.5a1 1 0 0 1 1 1c0 1.25.2 2.46.57 3.6a1 1 0 0 1-.25 1z"/></svg>
        0300-555-0142
      </li>
      <li class="contact-list__item">
        <svg class="contact-list__icon" viewBox="0 0 24 24" aria-hidden="true"><path d="M2 5h20v14H2zM3.5 6.5 12 12.5l8.5-6z" fill-rule="evenodd"/></svg>
        @yourweb.com
      </li>
      <li class="contact-list__item">
        <svg class="contact-list__icon" viewBox="0 0 24 24" aria-hidden="true" style="width:13px;height:13px;margin-right:8px"><path d="M12 2a7 7 0 0 0-7 7c0 5.25 7 13 7 13s7-7.75 7-13a7 7 0 0 0-7-7zm0 9.5A2.5 2.5 0 1 1 12 6.5a2.5 2.5 0 0 1 0 5z"/></svg>
        your address here
      </li>
    </ul>
  </section>

  <section class="card card--back" aria-label="Business card back">
    <div class="brand brand--back">
      <span class="brand__mark"></span>
      <span class="brand__name">Keystone Home Buyers</span>
    </div>
  </section>
</body>
</html>
```